Owen Tasker Studios Business Card

Looking for a clear, modern, elegant, sharp business card that conveys a professional yet edgy image to my business as a wedding, portrait, and travel photographer. Would like something that looks vintage yet modern. Need a new business card to grow my business. We are growing the business for Wedding and Event Photography as well as fine art Photography. (Mostly Landscapes)
Updates

I’m looking through designs now but I have a new logo that i want using please.

New logo uploaded please redesign using that

PLEASE ALL DESIGNERS LOOK IN BRIEF FOR NEW LOGO

Target Market(s)

Brides, Grooms, Families with Kids, People looking for Fine Art Photography Artwork

Industry/Entity Type

Photographer

Contact Information for Business Card

Unsure

Font styles to use
Serif

Colors

Designer to choose colors to be used in the design.

Requirements
Must have
• My Website:
• http://taskerlens.examplefolio.net
• Phone:
• 323-481-5206
• Email:
• owentaskerlens@mailbox-example.net
Nice to have
• Would like a sort of shine on the printing finish.
• I like black I think it looks good on a business card.
• Can try working with my logo (png that I've attached)

```html
<!DOCTYPE html>
<html lang="en">
<head>
<meta charset="utf-8">
<title>Owen Tasker Studios – Business Card</title>
<link rel="stylesheet" href="https://fonts.googleapis.com/css2?family=Cormorant+Garamond:wght@500;600&display=swap">
<style>
  :root {
    --backdrop: #6b6b6b;
    --card-light: #f2f2f2;
    --ink: #161616;
    --card-dark-top: #1a1a1a;
    --card-dark-mid: #0d0d0d;
    --card-dark-bottom: #050505;
    --pattern-tone: rgba(150, 150, 150, 0.16);
    --mark-light: #ffffff;
  }
  html, body {
    margin: 0;
    padding: 0;
    width: 1200px;
    height: 900px;
    overflow: hidden;
    background: var(--backdrop);
  }
  .stage {
    position: relative;
    width: 1200px;
    height: 900px;
  }
  .card {
    position: absolute;
    top: 170px;
    width: 347px;
    height: 561px;
    box-sizing: border-box;
    overflow: hidden;
  }
  .card-front {
    left: 259px;
    background: var(--card-light);
    color: var(--ink);
    text-align: center;
  }
  .card-back {
    left: 631px;
    background: linear-gradient(180deg, var(--card-dark-top) 0%, var(--card-dark-mid) 55%, var(--card-dark-bottom) 100%);
  }
  .brand-square {
    position: absolute;
    left: 134px;
    top: 125px;
    width: 78px;
    height: 78px;
    box-sizing: border-box;
    border: 2px solid var(--ink);
  }
  .brand-name {
    position: absolute;
    left: 0;
    right: 0;
    top: 226px;
    margin: 0;
    font-family: "Cormorant Garamond", serif;
    font-weight: 500;
    font-size: 37px;
    letter-spacing: 0.02em;
    line-height: 1;
  }
  .brand-tagline {
    position: absolute;
    left: 0;
    right: 0;
    top: 273px;
    margin: 0;
    font-family: "Cormorant Garamond", serif;
    font-weight: 500;
    font-size: 17px;
    letter-spacing: 0.45em;
    padding-left: 0.45em;
    line-height: 1;
  }
  .contact {
    position: absolute;
    left: 0;
    right: 0;
    top: 448px;
    margin: 0;
    font-family: "Cormorant Garamond", serif;
    font-weight: 600;
    font-size: 15.5px;
    line-height: 23.5px;
    font-style: normal;
    text-transform: uppercase;
  }
  .contact span { display: block; }
  .back-pattern {
    position: absolute;
    inset: 0;
    background:
      radial-gradient(ellipse 90% 55% at 50% 20%, var(--pattern-tone) 0%, rgba(150,150,150,0.06) 60%, rgba(0,0,0,0) 100%),
      linear-gradient(180deg, rgba(255,255,255,0.05) 0%, rgba(255,255,255,0) 70%);
  }
  .back-mark {
    position: absolute;
    left: 195px;
    top: 335px;
    width: 52px;
    height: 52px;
    box-sizing: border-box;
    border: 1.5px solid var(--mark-light);
  }
  .back-name {
    position: absolute;
    left: 141px;
    width: 160px;
    top: 396px;
    margin: 0;
    text-align: center;
    font-family: "Cormorant Garamond", serif;
    font-weight: 600;
    font-size: 12px;
    letter-spacing: 0.18em;
    line-height: 1;
    color: var(--mark-light);
    text-transform: uppercase;
  }
</style>
</head>
<body>
<main class="stage">
  <section class="card card-front">
    <div class="brand-square"></div>
    <h1 class="brand-name">OWEN TASKER</h1>
    <p class="brand-tagline">STUDIOS</p>
    <address class="contact">
      <span class="contact-phone">323-481-5206</span>
      <span class="contact-email">owentaskerlens@mailbox-example.net</span>
      <span class="contact-web">www.taskerlens.examplefolio.net</span>
    </address>
  </section>
  <section class="card card-back">
    <div class="back-pattern" role="img" aria-label="Faint repeating monogram pattern in soft grey on black, fading toward the bottom"></div>
    <div class="back-mark"></div>
    <p class="back-name">Owen Tasker</p>
  </section>
</main>
</body>
</html>
```